Letterhead for small civil engineer company

We need bold and modern design for company letterhead in MS word. It needs to have company logo and company info. Somewhere in the upper right part of document needs to be space for "recever" and the documents starts with, example, "SUBJECT: CIVIL ENGINEER LETTERHEAD".

in the bottom part of document needs to be signature and date.

Company info: Veltrana d.o.o., Lipovac 15, Lipovac (Općina Brdarić), OIB 47396028154, www.veltrana.hr, info@veltrana.hr

Email of document sender needs to be somewhere if document, exapmle xyz@veltrana.hr

Target Market(s)

Civil engineer company and projects

Industry/Entity Type

Civil engineer

Font styles to use
Serif

Colors
F0912C
F2A743
F7CA91
FBE8D2
FDF5EE

Requirements
Must have
• Company logo and company info
Nice to have
• Moder and clean design
Should not have
• Too much details

```html
<!DOCTYPE html>
<html lang="en">
<head>
<meta charset="utf-8">
<title>Veltrana d.o.o. – Letterhead</title>
<link href="https://fonts.googleapis.com/css2?family=Arimo:wght@400;700&display=swap" rel="stylesheet">
<style>
  :root {
    --paper: #e9e8e9;
    --ink: #3d3d3f;
    --ink-soft: #4a4a4c;
    --accent: #d9802e;
    --frame: #505052;
    --sign-area: #dcdadb;
  }
  * { margin: 0; padding: 0; box-sizing: border-box; }
  html, body { width: 950px; height: 1200px; overflow: hidden; }
  body {
    background: var(--paper);
    font-family: "Arimo", Arial, sans-serif;
    color: var(--ink);
  }
  .letterhead { position: relative; width: 950px; height: 1200px; }

  .rule { position: absolute; height: 1px; background: var(--accent); }
  .rule--top-left { left: 78px; top: 63px; width: 367px; }
  .rule--top-right { left: 549px; top: 63px; width: 326px; }
  .rule--bottom-left { left: 78px; top: 146px; width: 367px; }
  .rule--bottom-right { left: 549px; top: 146px; width: 326px; }

  .brand-square {
    position: absolute; left: 452px; top: 62px; width: 92px; height: 85px;
    border: 2px solid var(--frame);
  }
  .brand-name {
    position: absolute; left: 0; right: 0; top: 164px; text-align: center;
    font-size: 38px; font-weight: 700; letter-spacing: 1px; color: var(--accent);
    padding-left: 48px;
  }

  .company-info {
    position: absolute; left: 81px; top: 78px;
    font-size: 13px; line-height: 16px; color: var(--ink-soft);
  }
  .contact-list {
    position: absolute; right: 74px; top: 79px; list-style: none;
    font-size: 13px; line-height: 16px; color: var(--ink-soft); text-align: right;
  }
  .contact-list li { display: flex; justify-content: flex-end; align-items: center; gap: 8px; }
  .contact-list svg { width: 11px; height: 11px; flex: none; }

  .recipient {
    position: absolute; left: 71px; top: 338px;
    font-size: 15px; line-height: 16.5px; color: var(--ink);
  }
  .salutation {
    position: absolute; left: 73px; top: 466px;
    font-size: 16px; font-weight: 700; color: var(--ink);
  }
  .body-text {
    position: absolute; left: 73px; top: 527px; width: 810px;
    font-size: 14.6px; line-height: 16px; color: var(--ink);
  }
  .body-text p { margin-bottom: 16px; }

  .signatory { position: absolute; left: 76px; top: 866px; }
  .signatory__name { font-size: 17px; font-weight: 700; line-height: 22px; }
  .signatory__role { font-size: 17px; line-height: 22px; color: var(--ink-soft); }
  .signature {
    position: absolute; left: 73px; top: 922px; width: 155px; height: 75px;
    background: var(--sign-area);
  }
</style>
</head>
<body>
<main class="letterhead">
  <header>
    <div class="rule rule--top-left"></div>
    <div class="rule rule--top-right"></div>
    <div class="rule rule--bottom-left"></div>
    <div class="rule rule--bottom-right"></div>

    <address class="company-info" style="font-style:normal">
      Veltrana d.o.o.,<br>
      Lipovac 15, Lipovac (Općina Brdarić),<br>
      OIB 47396028154
    </address>

    <div class="brand-square"></div>
    <div class="brand-name">Veltrana</div>

    <ul class="contact-list">
      <li>+385 21 480 572
        <svg viewBox="0 0 12 12"><path fill="#d9802e" d="M2.5 1 4.3 1.2 5 3.6 3.9 4.5C4.5 5.9 5.7 7.2 7.3 7.9L8.3 6.8 10.6 7.6 10.8 9.4C10.2 10.6 8.8 11 7.6 10.5 4.8 9.4 2.5 7 1.4 4.3 1 3 1.3 1.7 2.5 1Z"/></svg>
      </li>
      <li>info@veltrana.hr
        <svg viewBox="0 0 12 12"><rect x="0.5" y="2.5" width="11" height="7.5" fill="#d9802e"/><path d="M0.8 2.8 6 6.8 11.2 2.8" fill="none" stroke="#e9e8e9" stroke-width="1"/></svg>
      </li>
      <li>www.veltrana.hr
        <svg viewBox="0 0 12 12"><circle cx="6" cy="6" r="5.5" fill="#d9802e"/><path d="M3 3.5 5.5 4 5 6.5 3.2 7.5M7.5 7 9.5 8.5 8 10" fill="none" stroke="#e9e8e9" stroke-width="1"/></svg>
      </li>
    </ul>
  </header>

  <section class="recipient">
    Mr Daniel Harlow<br>
    Founder and CEO<br>
    Your Company,<br>
    4120 Birchwood Avenue, Suite 210<br>
    Fairview, Canada 58213
  </section>

  <p class="salutation">Dear Sir</p>

  <section class="body-text">
    <p>Lorem ipsum dolor sit amet. Non quam iste ut dolor repellendus aut quasi porro nam molestias ullam ut sint ipsa! Qui accusamus assumenda qui quae tempore sit quia velit aut porro tempora. Est iste explicabo aut alias impedit est sequi quis.</p>
    <p>Cum rerum molestiae id galisum odit et autem voluptas aut blanditiis iste ut aspernatur itaque ut tempora laudantium vel voluptatem repudiandae! Ea delectus omnis est voluptas odit ut assumenda quisquam eos facere sunt qui quis vitae. Qui velit dolorem in distinctio</p>
    <p>dignissimos rem voluptatem totam ut quia nostrum cum quas consequuntur. Quo aliquid earum eum optio ducimus qui fugiat veniam qui blanditiis velit ut quos dolores non officiis enim ut voluptatem veritatis.</p>
    <p>At quia sunt nam quibusdam mollitia aut rerum laudantium et inventore molestiae aut cumque consequatur. 33 minima velit rem quasi galisum ut quae magni sed praesentium possimus 33 commodi quam qui quae aperiam est enim accusantium. Sed Quis laboriosam ut suscipit maxime cum reprehenderit adipisci. Non nihil dolor ut obcaecati commodi aut Quis provident eos doloribus cumque.</p>
    <p>At quia sunt nam quibusdam mollitia aut rerum laudantium et inventore molestiae aut cumque consequatur. 33 minima velit rem quasi galisum ut quae</p>
  </section>

  <footer>
    <div class="signatory">
      <div class="signatory__name">MARKO TENIĆ</div>
      <div class="signatory__role">President</div>
    </div>
    <div class="signature" role="img" aria-label="Handwritten signature of the president"></div>
  </footer>
</main>
</body>
</html>
```